PKD Business Card

Looking for a business card for my restaurant group I own. Four different concepts:

Bramblecrest Alehall
Vellory Alehall
Tamrack's Stone Hearth Kitchen
Cobblestead Patty Works

Card doesn't need to include all the logos.

```html
<!DOCTYPE html>
<html lang="en">
<head>
<meta charset="utf-8">
<title>PKD Business Card</title>
<link rel="stylesheet" href="https://fonts.googleapis.com/css2?family=Open+Sans:wght@400;600;700&display=swap">
<style>
  :root {
    --page: #ebebeb;
    --card: #1d1b1c;
    --gold: #c8ad72;
    --grey: #7c7b80;
    --ink-light: #f4f4f4;
    --font: "Open Sans", Arial, sans-serif;
  }
  * { box-sizing: border-box; margin: 0; padding: 0; }
  html, body {
    width: 1200px; height: 800px; overflow: hidden;
    background: var(--page);
    font-family: var(--font);
  }
  .card {
    position: absolute;
    left: 315px;
    width: 572px;
    height: 332px;
    background: var(--card);
    border-radius: 18px;
    overflow: hidden;
  }
  .card--front { top: 50px; }
  .card--back  { top: 418px; }

  /* Wordmark */
  .wordmark {
    position: absolute;
    display: flex; flex-direction: column; align-items: center;
    color: var(--gold);
    font-weight: 600;
    text-transform: uppercase;
    line-height: 1;
  }
  .wordmark__square {
    width: 30px; height: 30px;
    background: var(--gold);
    margin-bottom: 18px;
  }
  .wordmark__name { letter-spacing: 0.14em; }
  .wordmark__sub  { letter-spacing: 0.2em; }

  .card--front .wordmark { left: 0; right: 0; top: 104px; }
  .card--front .wordmark__name { font-size: 38px; }
  .card--front .wordmark__sub  { font-size: 17px; margin-top: 12px; }

  .card--back .wordmark { left: 392px; width: 164px; top: 46px; }
  .card--back .wordmark__square { width: 22px; height: 22px; margin-bottom: 14px; }
  .card--back .wordmark__name { font-size: 23px; letter-spacing: 0.1em; }
  .card--back .wordmark__sub  { font-size: 10.5px; margin-top: 8px; letter-spacing: 0.14em; }

  /* Back details */
  .name-tab {
    position: absolute; left: -6px; top: 61px;
    width: 14px; height: 40px;
    background: var(--gold);
    border-radius: 4px;
  }
  .holder__name {
    position: absolute; left: 20px; top: 54px;
    font-size: 20px; font-weight: 700; color: var(--gold);
  }
  .holder__company {
    position: absolute; left: 20px; top: 82px;
    font-size: 15px; color: var(--ink-light);
  }
  .contact {
    position: absolute; left: 20px; top: 213px;
    list-style: none;
    color: var(--ink-light);
    font-size: 15px;
  }
  .contact__item {
    display: flex; align-items: center;
    height: 20.5px;
  }
  .contact__icon {
    width: 11px; height: 11px;
    margin-right: 9px;
    fill: var(--gold);
  }
  .wave {
    position: absolute; left: 0; bottom: 0;
    width: 572px; height: 62px;
  }
</style>
</head>
<body>

<section class="card card--front" aria-label="Card front">
  <div class="wordmark">
    <span class="wordmark__square"></span>
    <span class="wordmark__name">Parkdale</span>
    <span class="wordmark__sub">Hospitality Group</span>
  </div>
</section>

<section class="card card--back" aria-label="Card back">
  <span class="name-tab"></span>
  <h1 class="holder__name">Dale Prewitt</h1>
  <p class="holder__company">Parkdale Hospitality Group</p>

  <div class="wordmark">
    <span class="wordmark__square"></span>
    <span class="wordmark__name">Parkdale</span>
    <span class="wordmark__sub">Hospitality Group</span>
  </div>

  <ul class="contact">
    <li class="contact__item">
      <svg class="contact__icon" viewBox="0 0 24 24"><path d="M6.6 10.8a15.1 15.1 0 0 0 6.6 6.6l2.2-2.2a1 1 0 0 1 1-.25 11.4 11.4 0 0 0 3.6.57 1 1 0 0 1 1 1V20a1 1 0 0 1-1 1A17 17 0 0 1 3 4a1 1 0 0 1 1-1h3.5a1 1 0 0 1 1 1c0 1.25.2 2.45.57 3.57a1 1 0 0 1-.25 1z"/></svg>
      555-014-2290
    </li>
    <li class="contact__item">
      <svg class="contact__icon" viewBox="0 0 24 24"><path d="M2 5h20v14H2z M4 7v1l8 5 8-5V7l-8 5z" fill-rule="evenodd"/></svg>
      dale@pkdrestaurants.com
    </li>
    <li class="contact__item">
      <svg class="contact__icon" viewBox="0 0 24 24"><circle cx="12" cy="12" r="10"/></svg>
      www.pkdrestaurants.com
    </li>
  </ul>

  <svg class="wave" viewBox="0 0 572 62" preserveAspectRatio="none" aria-hidden="true">
    <path d="M0,17 C120,40 220,46 300,38 C380,30 460,8 572,13 L572,62 L0,62 Z" fill="var(--gold)"/>
    <path d="M0,23 C120,47 220,51 300,43 C380,34 460,15 572,20 L572,62 L0,62 Z" fill="var(--card)"/>
    <path d="M0,27 C120,51 225,55 310,46 C390,37 465,19 572,24 L572,62 L0,62 Z" fill="var(--grey)"/>
    <path d="M0,30 C120,54 228,57 315,48 C395,39 468,23 572,28 L572,62 L0,62 Z" fill="var(--card)"/>
    <path d="M0,35 C120,58 232,60 320,51 C400,42 470,27 572,32 L572,62 L0,62 Z" fill="var(--gold)"/>
  </svg>
</section>

</body>
</html>
```